my personal cards just intrducing my self

Massage Therapy to get my name out their

Target Market(s)

40 year olds who enjoy massage

Industry/Entity Type

Massage

Contact Information for Business Card

Marcus L Tolhaven
LMT-Licensed Massage Therapist
*Swedish *Deep Tissue *Prenatal
*Reflexology *Chair and more

(738)-462-1937
marcustolhaven@mailbrook.net

Font styles to use
Serif

Colors
0456a4
6b449b

```html
<!DOCTYPE html>
<html lang="en">
<head>
<meta charset="utf-8">
<title>Marcus L Tolhaven LMT – Business Cards</title>
<link rel="stylesheet" href="https://fonts.googleapis.com/css2?family=Questrial&family=Tinos&display=swap">
<style>
  :root {
    --backdrop: #d9d9d9;
    --card-light: #f1f1f1;
    --card-mid: #dedede;
    --ink-blue: #1a4ea6;
    --ink-red: #e8322e;
    --mark-tint-a: #f6d3d0;
    --mark-tint-b: #eeb5b0;
  }
  html, body {
    margin: 0;
    width: 1200px;
    height: 960px;
    overflow: hidden;
  }
  body {
    background: linear-gradient(160deg, #c9c9c9 0%, var(--backdrop) 45%, #ececec 100%);
    position: relative;
    font-family: "Questrial", "Century Gothic", sans-serif;
  }
  .card {
    position: absolute;
    width: 500px;
    height: 286px;
    border-radius: 3px;
    background:
      repeating-linear-gradient(0deg, rgba(255,255,255,0.18) 0 1px, rgba(0,0,0,0.02) 1px 3px),
      linear-gradient(135deg, var(--card-light) 0%, var(--card-mid) 50%, var(--card-light) 100%);
    box-shadow: 0 14px 28px rgba(0,0,0,0.18), 0 2px 4px rgba(0,0,0,0.12);
    color: var(--ink-blue);
    text-align: center;
    box-sizing: border-box;
  }
  .card--back {
    left: 590px;
    top: 130px;
    padding-top: 30px;
  }
  .card--front {
    left: 120px;
    top: 500px;
    padding-top: 28px;
  }
  .services {
    list-style: none;
    margin: 0;
    padding: 0;
    font-size: 27px;
    line-height: 1.0;
  }
  .phone {
    margin: 18px 0 4px;
    font-family: "Tinos", "Times New Roman", serif;
    font-size: 19px;
    letter-spacing: 0.5px;
  }
  .email {
    margin: 0;
    font-size: 17px;
  }
  .logo-mark {
    display: block;
    margin: 0 auto;
  }
  .name {
    margin: 6px 0 0;
    font-size: 18px;
    color: var(--ink-blue);
  }
  .title {
    margin: 2px 0 0;
    font-size: 18px;
    color: var(--ink-red);
    letter-spacing: 0.4px;
  }
</style>
</head>
<body>
  <section class="card card--back">
    <ul class="services">
      <li>*Swedish</li>
      <li>*Deep Tissue</li>
      <li>*Prenatal Reflexology</li>
      <li>*Chair</li>
      <li>and more…</li>
    </ul>
    <p class="phone">(738)-462-1937</p>
    <p class="email">marcustolhaven@mailbrook.net</p>
  </section>

  <section class="card card--front">
    <svg class="logo-mark" width="170" height="170" viewBox="0 0 170 170" role="img" aria-label="Line illustration of a massage therapist working on a client, framed by a red circle">
      <defs>
        <radialGradient id="markTint" cx="50%" cy="45%" r="55%">
          <stop offset="0%" stop-color="var(--mark-tint-a)"/>
          <stop offset="100%" stop-color="var(--mark-tint-b)"/>
        </radialGradient>
      </defs>
      <circle cx="85" cy="85" r="80" fill="url(#markTint)"/>
    </svg>
    <p class="name">Marcus L Tolhaven LMT</p>
    <p class="title">Licensed Massage Therapist</p>
  </section>
</body>
</html>
```